New Property management company business cards

Looking for a new business card, to reflect new younger ownership
Card should be clean, simple and professional but with a modern layout that is conveys our new logo and business model

Key aspects of the business:

Property Management
Facility Maintenance
Project Management
Tenant Improvements

Mailing Address:
PO BOX 7186
Linden Falls CA, 95218

Phone: 209-614-8837
Direct: 209-614-8831

Doyle Farrant
President

Target Market(s)

Commercial property owners

Industry/Entity Type

Real Estate property management

Contact Information for Business Card

Open to all designs but lean toward vertical layouts

Requirements
Must have
• Logo and space to customize name and contact info

```html
<!DOCTYPE html>
<html lang="en">
<head>
<meta charset="utf-8">
<title>Verano Property Management – Business Card</title>
<link href="https://fonts.googleapis.com/css2?family=Montserrat:wght@400;500;700&display=swap" rel="stylesheet">
<style>
  :root {
    --teal: #1bb0aa;
    --teal-bright: #19b3ad;
    --ink: #37353c;
    --paper: #ffffff;
    --backdrop: #ffffff;
  }
  * { box-sizing: border-box; margin: 0; padding: 0; }
  html, body {
    width: 1200px; height: 2400px; overflow: hidden;
    background: var(--backdrop);
    font-family: "Montserrat", Arial, sans-serif;
    color: var(--ink);
  }
  .sheet { position: relative; width: 1200px; height: 2400px; }
  .card {
    position: absolute; left: 150px; width: 900px; height: 514px;
    box-shadow: 0 6px 40px rgba(0,0,0,0.10);
  }
  .card-front { top: 620px; background: var(--paper); }
  .card-back { top: 1222px; background: var(--teal); }

  .brand {
    position: absolute; left: 69px; top: 96px;
    display: flex; align-items: center; gap: 14px;
  }
  .brand-mark { width: 26px; height: 26px; background: var(--teal); flex: none; }
  .brand-text { display: flex; flex-direction: column; }
  .brand-name {
    font-size: 27px; font-weight: 500; letter-spacing: 5px; line-height: 1;
    text-transform: uppercase; color: var(--ink);
  }
  .brand-sub {
    font-size: 10px; font-weight: 500; letter-spacing: 3.6px; line-height: 1;
    text-transform: uppercase; color: var(--ink); margin-top: 5px;
  }

  .holder { position: absolute; right: 69px; top: 112px; text-align: right; }
  .holder-name {
    font-size: 25px; font-weight: 700; color: var(--teal-bright);
    text-transform: uppercase; line-height: 1.1;
  }
  .holder-title { font-size: 16px; font-weight: 500; text-transform: uppercase; margin-top: 4px; }

  .services { position: absolute; top: 253px; left: 0; width: 100%; list-style: none; }
  .service { position: absolute; font-size: 16px; line-height: 22px; font-weight: 400; }
  .service:nth-child(1) { left: 95px; }
  .service:nth-child(2) { left: 269px; }
  .service:nth-child(3) { left: 446px; }
  .service:nth-child(4) { left: 643px; }

  .divider {
    position: absolute; left: 68px; top: 312px; width: 736px; height: 2px; background: var(--ink);
  }
  .divider-end {
    position: absolute; left: 810px; top: 304px; width: 14px; height: 14px;
    border: 2px solid var(--teal);
  }

  .address {
    position: absolute; left: 68px; top: 398px;
    display: flex; gap: 12px; font-size: 20px; line-height: 27px;
  }
  .address svg { margin-top: 6px; flex: none; }

  .phones { position: absolute; right: 69px; top: 386px; font-size: 23px; line-height: 36px; }
  .phone { display: flex; align-items: center; gap: 12px; justify-content: flex-end; }

  .back-brand {
    position: absolute; left: 0; right: 0; top: 40px; bottom: 0;
    display: flex; align-items: center; justify-content: center; gap: 18px;
  }
  .back-brand .brand-mark { width: 40px; height: 40px; background: var(--ink); }
  .back-brand .brand-name { font-size: 42px; letter-spacing: 8px; }
  .back-brand .brand-sub { font-size: 14px; letter-spacing: 6px; margin-top: 8px; }
</style>
</head>
<body>
<main class="sheet">
  <section class="card card-front" aria-label="Business card front">
    <div class="brand">
      <span class="brand-mark"></span>
      <div class="brand-text">
        <span class="brand-name">Verano</span>
        <span class="brand-sub">Property Management</span>
      </div>
    </div>

    <div class="holder">
      <p class="holder-name">Doyle Farrant</p>
      <p class="holder-title">President</p>
    </div>

    <ul class="services">
      <li class="service">Property<br>Management</li>
      <li class="service">Facility<br>Maintenance</li>
      <li class="service">Project<br>Management</li>
      <li class="service">Tenant<br>Improvements</li>
    </ul>
    <div class="divider"></div>
    <div class="divider-end"></div>

    <div class="address">
      <svg width="14" height="18" viewBox="0 0 14 18" aria-hidden="true">
        <path d="M7 1a5.5 5.5 0 0 0-5.5 5.5C1.5 11 7 17 7 17s5.5-6 5.5-10.5A5.5 5.5 0 0 0 7 1z" fill="none" stroke="#1bb0aa" stroke-width="1.4"/>
        <circle cx="7" cy="6.5" r="2" fill="none" stroke="#1bb0aa" stroke-width="1.4"/>
      </svg>
      <p>Mailing Address:PO BOX 7186<br>Linden Falls CA, 95218</p>
    </div>

    <div class="phones">
      <p class="phone">
        <svg width="20" height="20" viewBox="0 0 24 24" aria-hidden="true"><path d="M6.6 2.5l3 3.6-1.9 2.3a13 13 0 0 0 7.9 7.9l2.3-1.9 3.6 3-1.8 3.3C12 20.7 3.3 12 2.5 4.3z" fill="none" stroke="#1bb0aa" stroke-width="1.4" stroke-linejoin="round"/><path d="M14 3.5a7 7 0 0 1 6.5 6.5M14 7a3.5 3.5 0 0 1 3 3" fill="none" stroke="#1bb0aa" stroke-width="1.4" stroke-linecap="round"/></svg>
        <span>209-614-8831</span>
      </p>
      <p class="phone">
        <svg width="20" height="20" viewBox="0 0 24 24" aria-hidden="true"><path d="M6.6 2.5l3 3.6-1.9 2.3a13 13 0 0 0 7.9 7.9l2.3-1.9 3.6 3-1.8 3.3C12 20.7 3.3 12 2.5 4.3z" fill="none" stroke="#1bb0aa" stroke-width="1.4" stroke-linejoin="round"/><path d="M14 3.5a7 7 0 0 1 6.5 6.5M14 7a3.5 3.5 0 0 1 3 3" fill="none" stroke="#1bb0aa" stroke-width="1.4" stroke-linecap="round"/></svg>
        <span>209-614-8837</span>
      </p>
    </div>
  </section>

  <section class="card card-back" aria-label="Business card back">
    <div class="back-brand">
      <span class="brand-mark"></span>
      <div class="brand-text">
        <span class="brand-name">Verano</span>
        <span class="brand-sub">Property Management</span>
      </div>
    </div>
  </section>
</main>
</body>
</html>
```